Business Card Design Project

We need a Business Card for an Mechanical Engineering firm in Singapore. The design should be Modern & Technical looking, yet eye catching.

Our company deals in Cutting Tools & Machine Accessories for the Manufacturing Industries such as Oil & Gas, Aero Space, etc... For more information on our Company, you can either email me or view our website www.valtrion.com.sg.

We are trying to revamp our image to give our consumers a fresh new perspective to our company, so we welcome all ideas.

Industry/Entity Type

Business

Requirements
Must have
• Must incorporate New Company Logo into the card as shown in Uploaded file.

```html
<!DOCTYPE html>
<html lang="en">
<head>
<meta charset="utf-8">
<title>Valtrion Tools – Business Card</title>
<link rel="stylesheet" href="https://fonts.googleapis.com/css2?family=Roboto+Condensed:wght@400;700&display=swap">
<style>
  :root {
    --card-brown: #6b5d53;
    --ink-dark: #463c35;
    --brand-red: #c8283a;
    --paper-white: #f4f1ee;
  }
  * { margin: 0; padding: 0; box-sizing: border-box; }
  html, body {
    width: 830px;
    height: 1200px;
    overflow: hidden;
    background: var(--card-brown);
  }
  .card {
    position: relative;
    width: 830px;
    height: 1200px;
    background: var(--card-brown);
    font-family: "Roboto Condensed", Arial, sans-serif;
    text-transform: uppercase;
  }
  .brand {
    position: absolute;
    top: 232px;
    right: 62px;
    display: flex;
    align-items: center;
    gap: 18px;
  }
  .brand-dot {
    width: 46px;
    height: 46px;
    border-radius: 50%;
    background: var(--brand-red);
  }
  .brand-name {
    font-weight: 400;
    font-size: 62px;
    letter-spacing: 1px;
    color: var(--paper-white);
    line-height: 1;
  }
  .person {
    position: absolute;
    top: 432px;
    left: 82px;
  }
  .person-name {
    font-weight: 400;
    font-size: 44px;
    color: var(--paper-white);
    letter-spacing: 1px;
  }
  .person-role {
    margin-top: 10px;
    font-weight: 700;
    font-size: 27px;
    color: var(--ink-dark);
    letter-spacing: 0.5px;
  }
  .contact {
    position: absolute;
    left: 82px;
    font-weight: 700;
    font-size: 31px;
    line-height: 1.3;
    color: var(--ink-dark);
  }
  .contact-address { top: 600px; }
  .contact-lines { top: 810px; }
  .footer-band {
    position: absolute;
    left: 0;
    bottom: 0;
    width: 100%;
    height: 160px;
    background: var(--brand-red);
  }
  .footer-band svg {
    position: absolute;
    left: 0;
    top: -22px;
  }
  .website {
    position: absolute;
    left: 82px;
    bottom: 52px;
    font-weight: 700;
    font-size: 36px;
    color: var(--paper-white);
    letter-spacing: 1px;
    text-transform: lowercase;
  }
</style>
</head>
<body>
  <main class="card">
    <div class="brand">
      <span class="brand-dot"></span>
      <span class="brand-name">VALTRION TOOLS</span>
    </div>

    <section class="person">
      <h1 class="person-name">Maren Holloway</h1>
      <p class="person-role">General Assistant</p>
    </section>

    <address class="contact contact-address" style="font-style:normal">
      Valtrion Tools Pte Ltd<br>
      27 Kestrel Loop #03-12,<br>
      Harbourline Business Hub,<br>
      Singapore 609871
    </address>

    <p class="contact contact-lines">
      Tel: 65-61230457<br>
      Fax: 65-61230458<br>
      maren@valtrion.com.sg
    </p>

    <footer class="footer-band">
      <svg width="830" height="24" viewBox="0 0 830 24" aria-hidden="true">
        <polygon points="0,24 560,24 580,12 610,12 620,2 660,2 672,10 700,10 712,18 830,18 830,24" fill="var(--brand-red)"/>
        <polyline points="0,23 560,23 580,11 610,11 620,1 660,1 672,9 700,9 712,17 830,17" fill="none" stroke="var(--paper-white)" stroke-width="2"/>
      </svg>
      <p class="website">www.valtrion.com.sg</p>
    </footer>
  </main>
</body>
</html>
```